Business card for a plastic surgeon

i need a business card for a plastic surgeon. I have two adresses. The card should communicate safety, simmetry, beauty and with soft colors.
What i want in the card:
- my logo: Letters "R"and "T" (picture uploaded)
- my name: Rodrigo Tavernelli
- my registration: CRM 527 319
- my adresses and phone numbers (2):
- Av Dr Bento Arruda, 2730, sala 408 - Vila Olímpia | São Paulo/ SP - Phone: 11 4721-6350
- Al. Itaquera, 61, 3 andar - Alphaville | Barueri/ SP - Phone: 11 5038-2917

- my social network: site, facebook and instagram

Target Market(s)

people (95% girls and women) that want cosmetic procedures and plastic surgery

Industry/Entity Type

Business

Contact Information for Business Card

The card should communicate safety, simmetry, beauty and with soft colors.
Beige, brown, gray, rosy are some options. Color is free

Font styles to use
Serif

Requirements
Must have
• - my logo: Letters "R"and "T" (picture uploaded)
• - my name: Rodrigo Tavernelli
• - my registration: CRM 527 319
• - my adresses and phone numbers (2):
• - Av Dr Bento Arruda, 2730, sala 408 - Vila Olímpia | São Paulo/ SP - Phone: 11 4721-6350
• - Al. Itaquera, 61, 3 andar - Alphaville | Barueri/ SP - Phone: 11 5038-2917
• - my social network: site, facebook and instagram
Should not have
• other images (only my logo)

```html
<!DOCTYPE html>
<html lang="pt-BR">
<head>
<meta charset="utf-8">
<title>Dr. Rodrigo Tavernelli – Cartão de visita</title>
<link rel="stylesheet" href="https://fonts.googleapis.com/css2?family=Cinzel:wght@400&family=Source+Serif+4:wght@300;400&display=swap">
<style>
  :root {
    --backdrop: #e4e4e2;
    --card: #43261a;
    --gold: #a98a5c;
    --gold-soft: #9c7f55;
    --cream: #d8c8b3;
    --shadow: rgba(0, 0, 0, 0.28);
  }
  * { box-sizing: border-box; margin: 0; padding: 0; }
  html, body { width: 1200px; height: 800px; overflow: hidden; }
  body {
    background: var(--backdrop);
    position: relative;
    font-family: "Source Serif 4", Georgia, serif;
    font-weight: 300;
    color: var(--gold);
  }
  .card {
    position: absolute;
    left: 320px;
    width: 560px;
    height: 320px;
    background: var(--card);
    box-shadow: 0 6px 18px var(--shadow);
  }
  .card-back { top: 50px; }
  .card-front { top: 420px; }
  .card-frame {
    position: absolute;
    inset: 16px;
    border: 1px solid var(--gold);
  }

  /* Back side */
  .back-name {
    position: absolute;
    left: 44px; top: 42px;
    font-size: 27px;
    font-weight: 400;
    color: var(--gold);
  }
  .back-reg {
    position: absolute;
    left: 46px; top: 80px;
    font-size: 14px;
  }
  .office {
    position: absolute;
    font-size: 15px;
    line-height: 1.3;
  }
  .office-sp { left: 50px; top: 134px; }
  .office-barueri { left: 322px; top: 86px; }
  .office .phone { margin-top: 14px; display: block; }
  .divider {
    position: absolute;
    left: 296px; top: 90px;
    width: 1px; height: 130px;
    background: var(--gold);
  }
  .social {
    position: absolute;
    font-size: 10px;
    letter-spacing: 0.06em;
    display: flex;
    align-items: center;
    gap: 5px;
  }
  .social::before {
    content: "";
    width: 5px; height: 5px;
    border-radius: 50%;
    background: var(--gold);
  }
  .social-profile { left: 44px; top: 270px; }
  .social-gallery { left: 270px; top: 262px; }
  .social-site { left: 470px; top: 250px; }

  /* Front side */
  .monogram {
    position: absolute;
    left: 0; right: 0; top: 62px;
    text-align: center;
    font-family: "Cinzel", "Times New Roman", serif;
    font-size: 72px;
    color: var(--gold);
    letter-spacing: 0.02em;
  }
  .front-name {
    position: absolute;
    left: 0; right: 0; top: 196px;
    text-align: center;
    font-family: "Cinzel", "Times New Roman", serif;
    font-size: 30px;
    color: var(--gold-soft);
  }
  .front-title {
    position: absolute;
    left: 0; right: 0; top: 240px;
    text-align: center;
    font-family: "Cinzel", "Times New Roman", serif;
    font-size: 15px;
    letter-spacing: 0.32em;
    color: var(--cream);
  }
</style>
</head>
<body>
  <section class="card card-back">
    <div class="card-frame"></div>
    <h1 class="back-name">DR. Rodrigo Tavernelli</h1>
    <p class="back-reg">registration: CRM 527 319</p>

    <address class="office office-sp">
      Av Dr Bento Arruda,<br>
      2730, sala 408<br>
      Vila Olímpia | São Paulo/ SP
      <span class="phone">Phone: 11 4721-6350</span>
    </address>

    <div class="divider"></div>

    <address class="office office-barueri">
      Al. Itaquera,<br>
      61, 3 andar<br>
      Alphaville | Barueri/ SP
      <span class="phone">Phone: 11 5038-2917</span>
    </address>

    <span class="social social-profile">profile</span>
    <span class="social social-gallery">gallery</span>
    <span class="social social-site">site</span>
  </section>

  <section class="card card-front">
    <div class="card-frame"></div>
    <div class="monogram">RT</div>
    <h2 class="front-name">DR. RODRIGO TAVERNELLI</h2>
    <p class="front-title">CIRURGIÃO PLÁSTICO</p>
  </section>
</body>
</html>
```